Label Design for Amber Kettle Specialty Coffee Roasters

We are a specialty coffee beans Roasting Shop named "Amber Kettle". We pack our beans in stand up poaches of varying sizes. We sell beans both to B2C and B2B and are looking to design stickers that will stand out. Our logo was designed with a black and white background. So far, we have been using white glossy bean bags and came up with a front label design that we would like to use for our labels.
We would like to see the design tweaked to fit both a white bag and a black one.
Currently, the attached front label design does not work on white bags. We would also like to have a back sticker designed that needs to include: 1- a description section for the type of beans used 2- a QR code section

Target Market(s)

Specialty beans in our area are typically liked by the younger generations 40 years and younger. Both male and females drink our coffee with varying income levels. But generally, middle class and above buy our coffee beans.

Requirements
Must have
• We are am looking for a sticker to be placed on a coffee bean bag. The sticker needs to contain the roasting shop's logo and brand name "Amber Kettle". Also, the sticker needs to have the following: country name, bean variety, weight (kg), roast date. The sticker needs to have the following specifications on a 5 point Likert scale (Strength, Fruitiness, Earthiness, Brightness). I uploaded a front label design that needs to be tweaked to fit both a white bag and a black one. The current design has owls representing the 5 point Likert scale and part of the shop's logo. We would like to keep that part of the design if possible. Currently, the attached front label design does not work on white bags.
We would also like to have a back sticker designed that needs to include: 1- a description section for the type of beans used 2- a QR code section
Nice to have
• The font that is used in the logo is League Gothic. It is okay to use this font or any other font if you find it more appropriate for the design.

```html
<!DOCTYPE html>
<html lang="en">
<head>
<meta charset="utf-8">
<title>Amber Kettle – Front Label</title>
<link rel="stylesheet" href="https://fonts.googleapis.com/css2?family=League+Gothic&display=swap">
<style>
  :root {
    --canvas-bg: #e9e9e9;
    --label-bg: #ffffff;
    --ink: #111111;
    --ink-muted: #bdbdbd;
    --ornament: #dcdcdc;
  }
  html, body {
    margin: 0;
    width: 1200px;
    height: 927px;
    overflow: hidden;
    background: var(--canvas-bg);
  }
  .canvas {
    width: 1200px;
    height: 927px;
    display: flex;
    align-items: center;
    justify-content: center;
  }
  .front-label {
    width: 641px;
    height: 841px;
    display: block;
    background: var(--label-bg);
    box-shadow: 0 2px 10px rgba(0,0,0,0.08);
  }
  .front-label text {
    font-family: "League Gothic", "Oswald", sans-serif;
    fill: var(--ink);
  }
  .arc-quote { font-size: 44px; }
  .brand-name { font-size: 70px; }
  .spec-head { font-size: 36px; letter-spacing: 1.5px; }
  .spec-label { font-size: 36px; letter-spacing: 1.5px; }
  .weight-label { font-size: 34px; letter-spacing: 1.5px; }
  .weight-value { font-size: 38px; letter-spacing: 1px; }
  .rule { stroke: var(--ink); stroke-width: 4; }
  .cup-on { color: var(--ink); }
  .cup-off { color: var(--ink-muted); }
  .ornament { fill: var(--ornament); }
  .brand-mark { fill: var(--ink); }
</style>
</head>
<body>
<main class="canvas">
  <svg class="front-label" viewBox="0 0 583 765" xmlns="http://www.w3.org/2000/svg" aria-label="Amber Kettle front coffee label">
    <defs>
      <path id="quote-arc" d="M81,365 A222,222 0 1,1 503,365"/>
      <symbol id="cup-icon" viewBox="0 0 40 38">
        <path d="M18 2 C14 6, 22 8, 18 13" fill="none" stroke="currentColor" stroke-width="1.6"/>
        <path d="M5 15 H31 V20 C31 28, 26 31, 18 31 C10 31, 5 28, 5 20 Z" fill="currentColor"/>
        <path d="M31 17 C38 17, 38 26, 30 26" fill="none" stroke="currentColor" stroke-width="3"/>
        <ellipse cx="18" cy="33.5" rx="16" ry="3" fill="currentColor"/>
      </symbol>
    </defs>

    <!-- corner ornaments -->
    <rect class="ornament" x="22" y="18" width="70" height="140" rx="10" role="img" aria-label="Decorative scroll ornament, top left"/>
    <rect class="ornament" x="491" y="18" width="70" height="140" rx="10" role="img" aria-label="Decorative scroll ornament, top right"/>
    <rect x="30" y="26" width="54" height="124" fill="var(--label-bg)" opacity="0.55"/>
    <rect x="499" y="26" width="54" height="124" fill="var(--label-bg)" opacity="0.55"/>

    <!-- curved quote -->
    <text class="arc-quote">
      <textPath href="#quote-arc" textLength="830" lengthAdjust="spacing">I DON'T NEED AN INSPIRATIONAL QUOTE. I NEED COFFEE.</textPath>
    </text>

    <!-- brand -->
    <circle class="brand-mark" cx="168" cy="260" r="30"/>
    <text class="brand-name" x="208" y="290" textLength="262" lengthAdjust="spacingAndGlyphs">AMBER KETTLE</text>

    <!-- table rules -->
    <line class="rule" x1="35" y1="418" x2="548" y2="418"/>
    <line class="rule" x1="311" y1="418" x2="311" y2="476"/>
    <line class="rule" x1="35" y1="476" x2="548" y2="476"/>
    <line class="rule" x1="433" y1="476" x2="433" y2="687"/>
    <line class="rule" x1="35" y1="687" x2="548" y2="687"/>
    <line class="rule" x1="35" y1="740" x2="548" y2="740"/>

    <text class="spec-head" x="52" y="461">COLOMBIA VARIETY</text>
    <text class="spec-head" x="348" y="461">100%ARABIC</text>

    <!-- ratings -->
    <g class="ratings">
      <text class="spec-label" x="35" y="525">STRENGHT</text>
      <use href="#cup-icon" class="cup-on" x="203" y="493" width="38" height="36"/>
      <use href="#cup-icon" class="cup-on" x="244" y="493" width="38" height="36"/>
      <use href="#cup-icon" class="cup-on" x="285" y="493" width="38" height="36"/>
      <use href="#cup-icon" class="cup-off" x="326" y="493" width="38" height="36"/>
      <use href="#cup-icon" class="cup-off" x="367" y="493" width="38" height="36"/>

      <text class="spec-label" x="35" y="575">FRUITINESS</text>
      <use href="#cup-icon" class="cup-on" x="203" y="543" width="38" height="36"/>
      <use href="#cup-icon" class="cup-off" x="244" y="543" width="38" height="36"/>
      <use href="#cup-icon" class="cup-off" x="285" y="543" width="38" height="36"/>
      <use href="#cup-icon" class="cup-off" x="326" y="543" width="38" height="36"/>
      <use href="#cup-icon" class="cup-off" x="367" y="543" width="38" height="36"/>

      <text class="spec-label" x="35" y="625">EARTHINESS</text>
      <use href="#cup-icon" class="cup-on" x="203" y="593" width="38" height="36"/>
      <use href="#cup-icon" class="cup-on" x="244" y="593" width="38" height="36"/>
      <use href="#cup-icon" class="cup-on" x="285" y="593" width="38" height="36"/>
      <use href="#cup-icon" class="cup-off" x="326" y="593" width="38" height="36"/>
      <use href="#cup-icon" class="cup-off" x="367" y="593" width="38" height="36"/>

      <text class="spec-label" x="35" y="675">BRIGHTNESS</text>
      <use href="#cup-icon" class="cup-on" x="203" y="643" width="38" height="36"/>
      <use href="#cup-icon" class="cup-on" x="244" y="643" width="38" height="36"/>
      <use href="#cup-icon" class="cup-off" x="285" y="643" width="38" height="36"/>
      <use href="#cup-icon" class="cup-off" x="326" y="643" width="38" height="36"/>
      <use href="#cup-icon" class="cup-off" x="367" y="643" width="38" height="36"/>
    </g>

    <!-- weight -->
    <text class="weight-label" x="447" y="570">WEIGTH</text>
    <text class="weight-value" x="451" y="614">250 G</text>

    <!-- roast date -->
    <text class="spec-label" x="60" y="729">ROAST DATE:</text>
  </svg>
</main>
</body>
</html>
```